Roofing Company Sales Rep Business Card

Business card for sales rep to canvass and hand out to property owners/managers for free roof inspections and roof replacements.

```html
<!DOCTYPE html>
<html lang="en">
<head>
<meta charset="utf-8">
<title>Ridgeline Roofing – Business Card</title>
<link href="https://fonts.googleapis.com/css2?family=Montserrat:wght@400;500;700;800&display=swap" rel="stylesheet">
<style>
  :root {
    --brand-red: #e01b24;
    --ink: #111111;
    --text: #1d1d1d;
    --card: #ffffff;
    --stage: #dcdcda;
  }
  * { box-sizing: border-box; margin: 0; padding: 0; }
  html, body { width: 1200px; height: 801px; overflow: hidden; }
  body {
    background: var(--stage);
    font-family: "Montserrat", sans-serif;
    display: flex;
    align-items: center;
    justify-content: center;
    gap: 40px;
  }
  .card {
    position: relative;
    width: 540px;
    height: 309px;
    background: var(--card);
    border-radius: 22px;
    border-bottom: 4px solid var(--brand-red);
    overflow: hidden;
    box-shadow: 0 10px 24px rgba(0,0,0,0.18);
  }
  /* Front side */
  .card-front .accent-block {
    position: absolute;
    left: 0;
    top: 62px;
    width: 34px;
    height: 44px;
    background: var(--brand-red);
  }
  .contact {
    position: absolute;
    left: 56px;
    top: 58px;
    color: var(--text);
  }
  .contact-name {
    color: var(--brand-red);
    font-weight: 800;
    font-size: 21px;
    letter-spacing: 0.5px;
    line-height: 1.1;
  }
  .contact-title {
    font-size: 15px;
    font-weight: 400;
    margin-top: 2px;
  }
  .contact-list {
    list-style: none;
    margin-top: 18px;
    font-size: 14px;
    line-height: 22px;
  }
  .contact-list li { display: flex; align-items: center; gap: 8px; }
  .contact-list svg { width: 12px; height: 12px; fill: var(--brand-red); flex: none; }
  .contact-address {
    margin-top: 18px;
    margin-left: 20px;
    font-size: 14px;
    line-height: 20px;
  }
  .brand {
    position: absolute;
    display: flex;
    align-items: center;
    gap: 10px;
    color: var(--ink);
    font-weight: 800;
    white-space: nowrap;
  }
  .card-front .brand {
    right: 30px;
    top: 80px;
    font-size: 20px;
    letter-spacing: 1px;
  }
  .brand-mark {
    background: var(--brand-red);
    flex: none;
  }
  .card-front .brand-mark { width: 14px; height: 14px; }
  /* Back side */
  .card-back .brand {
    left: 50%;
    top: 50%;
    transform: translate(-50%, -50%);
    font-size: 34px;
    letter-spacing: 1.5px;
    gap: 14px;
  }
  .card-back .brand-mark { width: 24px; height: 24px; }
</style>
</head>
<body>
  <section class="card card-front" aria-label="Business card front">
    <div class="accent-block"></div>
    <div class="contact">
      <h1 class="contact-name">DANIEL HARTWELL</h1>
      <p class="contact-title">Managing Director</p>
      <ul class="contact-list">
        <li>
          <svg viewBox="0 0 24 24" aria-hidden="true"><path d="M6.6 10.8a15.1 15.1 0 0 0 6.6 6.6l2.2-2.2a1 1 0 0 1 1-.25 11.4 11.4 0 0 0 3.6.57 1 1 0 0 1 1 1V20a1 1 0 0 1-1 1A17 17 0 0 1 3 4a1 1 0 0 1 1-1h3.5a1 1 0 0 1 1 1c0 1.25.2 2.45.57 3.6a1 1 0 0 1-.25 1z"/></svg>
          555 204 318
        </li>
        <li>
          <svg viewBox="0 0 24 24" aria-hidden="true"><path d="M2 5h20v14H2z M2 5l10 8 10-8" fill="var(--brand-red)"/><path d="M3 6l9 7 9-7" fill="none" stroke="#fff" stroke-width="2"/></svg>
          hello@ridgelinemail.com
        </li>
        <li>
          <svg viewBox="0 0 24 24" aria-hidden="true"><circle cx="12" cy="12" r="10"/><path d="M2 12h20M12 2c3 3 3 17 0 20M12 2c-3 3-3 17 0 20" fill="none" stroke="#fff" stroke-width="1.5"/></svg>
          www.ridgelineroofs.com
        </li>
      </ul>
      <p class="contact-address">Your address, City<br>State, Zip 1234</p>
    </div>
    <div class="brand"><span class="brand-mark"></span>RIDGELINE ROOFING</div>
  </section>

  <section class="card card-back" aria-label="Business card back">
    <div class="brand"><span class="brand-mark"></span>RIDGELINE ROOFING</div>
  </section>
</body>
</html>
```